Looking for power point temple for video course

Need slides which will be used to create a video course titled

“Wireless Packet Forensics Workshop”

The course will have lots of slide content and also lots of video screen dlow

Iooking for professional grade designs that match my logo and color scheme: Red Grey & white

Other colors shades are welcome so log as they do not clash with the primary colors.

Like Vectors!

Target Market(s)

Information Security & IT

Industry/Entity Type

Security

Requirements
Must have
• Six separate power point slides;
• 1 Cover slide
• 1 table of contents slide
• 2 heading slides 1 light 1 dark
• 2 content aides 1 light 1 dark
• Match the color and theme of my logo
• Look professional
Nice to have
• Custom bullets, icons, charts tables. All should flow with a uniform theme thought the slide template
Should not have
• Not too many stock photos. It’s fine to have a few faded background type images but I want the focus to be on content and on Vectors

```html
<!DOCTYPE html>
<html lang="en">
<head>
<meta charset="utf-8">
<title>Wireless Packet Forensics Workshop – Slide Template</title>
<link href="https://fonts.googleapis.com/css2?family=Montserrat:wght@400;600;700;800&family=Roboto:wght@400;500&display=swap" rel="stylesheet">
<style>
:root{
  --red:#e2202a;
  --red-dark:#b5141d;
  --dark:#3a3f47;
  --darker:#2c3037;
  --grey:#8a8f97;
  --grey-light:#d7d9dc;
  --paper:#ffffff;
  --canvas:#f1f1f1;
}
*{box-sizing:border-box;margin:0;padding:0}
html,body{width:1200px;height:2304px;overflow:hidden;background:var(--canvas)}
body{font-family:"Roboto",Arial,sans-serif;color:var(--dark)}
.deck{display:grid;grid-template-columns:590px 590px;grid-auto-rows:322px;gap:8px;padding:1px 6px}
.slide{position:relative;overflow:hidden;background:var(--paper);box-shadow:0 1px 3px rgba(0,0,0,.15)}
.slide.dark{background:var(--dark);color:#fff}
.h{font-family:"Montserrat",Arial,sans-serif}
.brand{font-family:"Montserrat",Arial,sans-serif;font-weight:800;font-size:15px;letter-spacing:.5px;display:flex;align-items:center;gap:6px;color:#fff}
.brand .mark{width:10px;height:10px;background:var(--red);display:inline-block}
.brand.on-light{color:var(--dark)}
.brand.small{font-size:10px}
.brand.small .mark{width:7px;height:7px}
.slide-title{position:absolute;left:22px;top:16px;font-family:"Montserrat",Arial,sans-serif;font-weight:800;font-size:17px;letter-spacing:.5px}
.slide-title em{font-style:normal;color:var(--red)}
.foot-brand{position:absolute;left:22px;bottom:12px}
.foot-dot{position:absolute;right:16px;bottom:14px;width:9px;height:9px;border-radius:50%;background:var(--red)}
.placeholder{position:absolute}
.txt{font-size:9px;line-height:1.4;color:var(--grey)}
.label{font-family:"Montserrat",Arial,sans-serif;font-weight:700;font-size:10px}
/* cover */
.cover-bar{position:absolute;left:0;top:0;right:0;height:50px;background:var(--darker);display:flex;align-items:center;padding-left:24px}
.cover-title{position:absolute;left:34px;top:95px;font-family:"Montserrat",Arial,sans-serif;font-weight:700;font-size:26px;line-height:1.2;color:#fff}
.cover-title em{font-style:normal;color:var(--red)}
/* agenda */
.agenda{position:absolute;left:330px;top:46px;display:flex;flex-direction:column;gap:14px}
.agenda li{list-style:none;display:flex;align-items:center;gap:14px}
.diamond{width:28px;height:28px;background:#fff;transform:rotate(45deg);display:flex;align-items:center;justify-content:center}
.diamond i{width:10px;height:10px;background:var(--red);display:block}
/* team */
.team{position:absolute;left:22px;right:22px;top:56px;display:grid;grid-template-columns:repeat(4,1fr);gap:14px}
.bar{height:5px;background:var(--grey-light);margin-top:5px}
.bar span{display:block;height:100%;background:var(--red)}
/* table */
.table{position:absolute;left:40px;right:40px;top:56px;border-collapse:collapse;font-size:9px;color:var(--dark)}
.table th{font-family:"Montserrat",Arial,sans-serif;font-size:9px;color:#fff;padding:6px;background:var(--grey)}
.table th.red{background:var(--red)}
.table th.blank{background:transparent}
.table td{background:#fff;border:1px solid var(--grey-light);padding:6px;text-align:center}
.table td.row-head{background:var(--darker);color:#fff;text-align:left;border-color:var(--dark)}
.btn{display:inline-block;padding:3px 8px;border-radius:8px;background:var(--dark);color:#fff;font-size:8px}
.btn.red{background:var(--red)}
</style>
</head>
<body>
<main class="deck">

  <!-- Cover, dark -->
  <section class="slide dark">
    <div class="cover-bar"><span class="brand"><i class="mark"></i>PACKETLAB</span></div>
    <div class="placeholder" role="img" aria-label="Faded network hardware background image" style="left:300px;top:50px;right:0;bottom:0;background:linear-gradient(90deg,var(--dark),#4b5058)"></div>
    <h1 class="cover-title"><em>WIRELESS PACKET</em><br>FORENSICS <em>WORKSHOP</em></h1>
  </section>

  <!-- Cover, light -->
  <section class="slide">
    <svg width="590" height="322" style="position:absolute;left:0;top:0">
      <polygon points="150,20 590,20 590,90 110,90" fill="var(--red)"/>
      <polygon points="110,90 590,90 590,96 106,96" fill="var(--dark)"/>
    </svg>
    <h1 class="h" style="position:absolute;left:150px;top:32px;color:#fff;font-weight:700;font-size:19px;line-height:1.2">WIRELESS PACKET<br>FORENSICS WORKSHOP</h1>
    <p class="txt" style="position:absolute;left:150px;top:104px;color:var(--dark)">www.packetlab-academy.com</p>
    <div class="brand on-light" style="position:absolute;right:24px;top:122px"><i class="mark"></i>PACKETLAB</div>
  </section>

  <!-- Heading slide, light -->
  <section class="slide">
    <svg width="590" height="322" style="position:absolute;left:0;top:0">
      <polygon points="0,0 590,0 590,70 0,150" fill="var(--dark)"/>
      <polygon points="250,120 590,72 590,110 200,160" fill="var(--red)"/>
      <polygon points="0,150 590,70 590,76 0,158" fill="var(--darker)"/>
    </svg>
    <div class="brand" style="position:absolute;left:24px;top:20px"><i class="mark"></i>PACKETLAB</div>
    <h2 class="h" style="position:absolute;left:0;right:0;top:200px;text-align:center;font-weight:600;font-size:22px;line-height:1.25"><span style="color:var(--red)">WIRELESS PACKET</span><br><span style="color:var(--dark)">FORENSICS WORKSHOP</span></h2>
  </section>

  <!-- Table of contents -->
  <section class="slide dark">
    <div class="placeholder" role="img" aria-label="Faded technology background image" style="left:0;top:0;width:290px;bottom:0;background:linear-gradient(135deg,#50555d,var(--darker))"></div>
    <h2 class="slide-title">OUR <em>CONTENT</em></h2>
    <ul class="agenda">
      <li><span class="diamond"><i></i></span><div><p class="label">Agenda One</p><p class="txt" style="color:#c3c6ca">Capture setup and tools</p></div></li>
      <li><span class="diamond"><i></i></span><div><p class="label">Agenda Two</p><p class="txt" style="color:#c3c6ca">Reading wireless frame headers</p></div></li>
      <li><span class="diamond"><i></i></span><div><p class="label">Agenda Three</p><p class="txt" style="color:#c3c6ca">Finding rogue access points</p></div></li>
      <li><span class="diamond"><i></i></span><div><p class="label">Agenda Four</p><p class="txt" style="color:#c3c6ca">Reporting your evidence trail</p></div></li>
    </ul>
    <div class="foot-brand brand small"><i class="mark"></i>PACKETLAB</div>
  </section>

  <!-- Malware protection -->
  <section class="slide dark">
    <h2 class="slide-title">MALWARE <em>PROTECTION</em></h2>
    <div class="placeholder" role="img" aria-label="Vector illustration of a laptop with a shield, lock and cloud icons" style="left:130px;top:70px;width:330px;height:200px;background:radial-gradient(ellipse at center,#e7e8ea 0%,#b9bcc1 55%,var(--dark) 75%)"></div>
    <div class="foot-brand brand small"><i class="mark"></i>PACKETLAB</div>
  </section>

  <!-- Key features -->
  <section class="slide">
    <h2 class="slide-title" style="color:var(--dark)">KEY <em>FEATURES</em></h2>
    <div class="placeholder" role="img" aria-label="Dark photo of a laptop showing code" style="left:300px;top:50px;right:0;height:200px;background:linear-gradient(120deg,var(--darker),#6b7077)"></div>
    <div style="position:absolute;left:24px;top:80px;display:flex;gap:20px">
      <div style="text-align:center"><svg width="30" height="30"><circle cx="15" cy="15" r="14" fill="var(--red)"/><path d="M9 15l4 4 8-8" stroke="#fff" stroke-width="2.5" fill="none"/></svg><p class="label">Live Capture</p></div>
      <div style="text-align:center"><svg width="30" height="30"><circle cx="15" cy="15" r="14" fill="var(--dark)"/><path d="M9 15l4 4 8-8" stroke="#fff" stroke-width="2.5" fill="none"/></svg><p class="label">Deep Filters</p></div>
      <div style="text-align:center"><svg width="30" height="30"><circle cx="15" cy="15" r="14" fill="var(--grey)"/><path d="M9 15l4 4 8-8" stroke="#fff" stroke-width="2.5" fill="none"/></svg><p class="label">Clear Reports</p></div>
    </div>
    <p class="txt" style="position:absolute;left:24px;top:150px;width:250px"><b style="color:var(--dark)">Hands-on labs</b> walk you through each stage of a wireless investigation, from first capture to final findings.</p>
    <div class="foot-dot"></div>
  </section>

  <!-- Team -->
  <section class="slide">
    <h2 class="slide-title" style="color:var(--dark)">MEET <em>THE TEAM</em></h2>
    <div class="team">
      <div><div role="img" aria-label="Portrait photo of team member" style="height:100px;background:linear-gradient(#e3e4e6,#b8bbc0)"></div><p class="label" style="margin-top:6px">Alex Ray</p><p class="txt">Lead Analyst</p><div class="bar"><span style="width:80%"></span></div><div class="bar"><span style="width:60%;background:var(--dark)"></span></div></div>
      <div><div role="img" aria-label="Portrait photo of team member" style="height:100px;background:linear-gradient(#e3e4e6,#b8bbc0)"></div><p class="label" style="margin-top:6px">Mara Lin</p><p class="txt">Lab Designer</p><div class="bar"><span style="width:70%"></span></div><div class="bar"><span style="width:85%;background:var(--dark)"></span></div></div>
      <div><div role="img" aria-label="Portrait photo of team member" style="height:100px;background:linear-gradient(#e3e4e6,#b8bbc0)"></div><p class="label" style="margin-top:6px">Owen Park</p><p class="txt">RF Engineer</p><div class="bar"><span style="width:90%"></span></div><div class="bar"><span style="width:55%;background:var(--dark)"></span></div></div>
      <div><div role="img" aria-label="Portrait photo of team member" style="height:100px;background:linear-gradient(#e3e4e6,#b8bbc0)"></div><p class="label" style="margin-top:6px">Tess Moore</p><p class="txt">Course Host</p><div class="bar"><span style="width:65%"></span></div><div class="bar"><span style="width:75%;background:var(--dark)"></span></div></div>
    </div>
    <div class="foot-brand brand small on-light"><i class="mark"></i>PACKETLAB</div>
  </section>

  <!-- Project design -->
  <section class="slide">
    <h2 class="slide-title" style="color:var(--dark)">PROJECT <em>DESIGN</em></h2>
    <svg width="200" height="200" style="position:absolute;left:195px;top:60px">
      <polygon points="100,120 190,150 100,180 10,150" fill="var(--grey)"/>
      <polygon points="100,95 190,125 100,155 10,125" fill="var(--dark)"/>
      <polygon points="100,70 190,100 100,130 10,100" fill="var(--red-dark)"/>
      <polygon points="100,45 190,75 100,105 10,75" fill="var(--red)"/>
      <polygon points="100,20 190,50 100,80 10,50" fill="#f0a3a7"/>
    </svg>
    <div style="position:absolute;left:40px;top:90px;width:140px;text-align:right"><p class="label" style="color:var(--red)">Capture</p><p class="txt">Collect raw air traffic</p></div>
    <div style="position:absolute;left:40px;top:170px;width:140px;text-align:right"><p class="label">Decode</p><p class="txt">Parse frames and flows</p></div>
    <div style="position:absolute;left:410px;top:90px;width:140px"><p class="label" style="color:var(--red)">Analyse</p><p class="txt">Spot anomalies and threats</p></div>
    <div style="position:absolute;left:410px;top:170px;width:140px"><p class="label">Report</p><p class="txt">Document the final evidence</p></div>
    <div class="foot-dot"></div>
  </section>

  <!-- Chainlink process -->
  <section class="slide">
    <h2 class="slide-title" style="color:var(--dark)">CHAINLINK <em>PROCESS</em></h2>
    <svg width="590" height="160" style="position:absolute;left:0;top:80px">
      <path d="M70 70 Q120 10 170 70 T270 70 T370 70 T470 70 T520 70" stroke="var(--grey-light)" stroke-width="10" fill="none"/>
      <circle cx="70" cy="70" r="30" fill="var(--red)"/><circle cx="70" cy="70" r="18" fill="#fff"/>
      <circle cx="170" cy="70" r="30" fill="var(--dark)"/><circle cx="170" cy="70" r="18" fill="#fff"/>
      <circle cx="270" cy="70" r="30" fill="var(--red)"/><circle cx="270" cy="70" r="18" fill="#fff"/>
      <circle cx="370" cy="70" r="30" fill="var(--dark)"/><circle cx="370" cy="70" r="18" fill="#fff"/>
      <circle cx="470" cy="70" r="30" fill="var(--red)"/><circle cx="470" cy="70" r="18" fill="#fff"/>
    </svg>
    <div style="position:absolute;left:20px;right:70px;top:195px;display:grid;grid-template-columns:repeat(5,1fr);text-align:center">
      <div><p class="label">Scan</p><p class="txt">Find networks</p></div>
      <div><p class="label">Capture</p><p class="txt">Record packets</p></div>
      <div><p class="label">Filter</p><p class="txt">Trim the noise</p></div>
      <div><p class="label">Inspect</p><p class="txt">Read the frames</p></div>
      <div><p class="label">Report</p><p class="txt">Share findings</p></div>
    </div>
    <div class="foot-brand brand small on-light"><i class="mark"></i>PACKETLAB</div>
  </section>

  <!-- Simple table -->
  <section class="slide dark">
    <h2 class="slide-title">SIMPLE <em>TABLE</em></h2>
    <table class="table">
      <tr><th class="blank"></th><th>Basic</th><th class="red">Standard</th><th>Pro</th><th class="red">Team</th></tr>
      <tr><td class="row-head">Video lessons</td><td>✓</td><td>✓</td><td>✓</td><td>✓</td></tr>
      <tr><td class="row-head">Lab files</td><td>–</td><td>✓</td><td>✓</td><td>✓</td></tr>
      <tr><td class="row-head">Live sessions</td><td>–</td><td>–</td><td>✓</td><td>✓</td></tr>
      <tr><td class="row-head">Certificate</td><td>–</td><td>✓</td><td>✓</td><td>✓</td></tr>
      <tr><td class="row-head">Support</td><td><span class="btn">Join Now</span></td><td><span class="btn red">Join Now</span></td><td><span class="btn">Join Now</span></td><td><span class="btn red">Join Now</span></td></tr>
    </table>
    <div class="foot-brand brand small"><i class="mark"></i>PACKETLAB</div>
  </section>

  <!-- Light content -->
  <section class="slide">
    <h2 class="slide-title" style="color:var(--dark)">YOUR LIGHT <em>CONTENT SLIDE</em></h2>
    <div class="foot-dot"></div>
  </section>

  <!-- Dark content -->
  <section class="slide dark">
    <h2 class="slide-title">YOUR DARK <em>CONTENT SLIDE</em></h2>
    <div class="foot-dot"></div>
  </section>

  <!-- Thank you with feedback -->
  <section class="slide dark">
    <div class="placeholder" role="img" aria-label="Faded photo of a hand holding a smartphone over a desk" style="left:250px;top:0;right:0;bottom:0;background:linear-gradient(90deg,var(--dark),#9a9ea4)"></div>
    <div class="brand" style="position:absolute;left:24px;top:20px"><i class="mark"></i>PACKETLAB</div>
    <h2 class="h" style="position:absolute;left:24px;top:150px;font-weight:800;font-size:34px">THANK <span style="color:var(--red)">YOU</span></h2>
    <p class="h" style="position:absolute;left:24px;top:192px;font-size:11px;font-weight:600">Send Your Feedback</p>
    <ul style="position:absolute;left:24px;top:225px;list-style:none;font-size:8px;line-height:1.9;color:#c3c6ca">
      <li><span style="color:var(--red)">●</span> 42 Relay Street, Portside</li>
      <li><span style="color:var(--red)">●</span> +1 555 014 2290</li>
      <li><span style="color:var(--red)">●</span> hello@packetlab-academy.com</li>
      <li><span style="color:var(--red)">●</span> www.packetlab-academy.com</li>
    </ul>
  </section>

  <!-- Thank you, dark -->
  <section class="slide dark">
    <svg width="590" height="322" style="position:absolute;left:0;top:0">
      <polygon points="0,0 590,0 590,40 0,90" fill="#4a4f57"/>
      <polygon points="0,90 590,40 590,48 0,98" fill="var(--red)"/>
    </svg>
    <div class="brand" style="position:absolute;left:0;right:0;top:150px;justify-content:center;font-size:20px"><i class="mark" style="width:14px;height:14px"></i>PACKETLAB</div>
    <h2 class="h" style="position:absolute;left:0;right:0;top:205px;text-align:center;font-weight:700;font-size:26px">THANK <span style="color:var(--red)">YOU</span></h2>
  </section>

</main>
</body>
</html>
```